Quillan Bay Clinics
Mobile Ultrasound Services
Professional
Doreen T. Falkner
Chief Operations Officer
837 Township Lane 212
Brookvale, GA 30114
quillanbayclinics@mailvista.net
www.quillanbayclinicsco.net
Logo Files

```html
<!DOCTYPE html>
<html lang="en">
<head>
<meta charset="utf-8">
<title>Quillan Bay Clinics – Business Card</title>
<link rel="stylesheet" href="https://fonts.googleapis.com/css2?family=Open+Sans:wght@400;600;700&display=swap">
<style>
  :root {
    --page-bg: #eceae6;
    --card-bg: #ffffff;
    --brand-blue: #1b7fc9;
    --brand-grey: #6f7275;
    --swoosh-grey: #9a9da0;
    --text-dark: #2b2b2b;
    --divider: #3a3a3a;
  }
  html, body {
    margin: 0;
    padding: 0;
    width: 1200px;
    height: 775px;
    overflow: hidden;
    background: var(--page-bg);
    font-family: "Open Sans", Arial, sans-serif;
  }
  .card {
    position: absolute;
    left: 50px;
    top: 68px;
    width: 1100px;
    height: 640px;
    background: var(--card-bg);
    border-radius: 40px;
    overflow: hidden;
    box-shadow: 0 2px 6px rgba(0,0,0,0.12);
  }
  .brand {
    position: absolute;
    left: 180px;
    top: 100px;
    display: flex;
    align-items: center;
    gap: 20px;
  }
  .brand-dot {
    width: 52px;
    height: 52px;
    border-radius: 50%;
    background: var(--brand-blue);
  }
  .brand-name {
    font-size: 54px;
    font-weight: 700;
    color: var(--brand-grey);
    letter-spacing: 0.5px;
  }
  .person {
    position: absolute;
    right: 610px;
    top: 245px;
    text-align: right;
    white-space: nowrap;
  }
  .person-name {
    font-size: 33px;
    font-weight: 600;
    color: var(--brand-blue);
    line-height: 1.15;
  }
  .person-title {
    font-size: 23px;
    font-weight: 700;
    color: var(--text-dark);
    margin-top: 4px;
  }
  .person-address {
    font-size: 26px;
    color: var(--text-dark);
    margin-top: 22px;
    line-height: 1.45;
  }
  .divider {
    position: absolute;
    left: 506px;
    top: 250px;
    width: 2px;
    height: 225px;
    background: var(--divider);
  }
  .contacts {
    position: absolute;
    left: 526px;
    top: 245px;
    list-style: none;
    margin: 0;
    padding: 0;
  }
  .contacts li {
    display: flex;
    align-items: center;
    height: 46px;
    font-size: 27px;
    color: var(--text-dark);
    white-space: nowrap;
  }
  .contacts .icon {
    width: 28px;
    height: 28px;
    margin-right: 14px;
    flex: none;
    fill: var(--brand-blue);
    color: var(--brand-blue);
  }
  .contacts .icon-globe {
    fill: none;
    stroke: var(--brand-blue);
    stroke-width: 2;
  }
  .contacts .icon-at {
    font-weight: 700;
    font-size: 28px;
    line-height: 28px;
    text-align: center;
  }
  .swoosh {
    position: absolute;
    left: 0;
    bottom: 0;
    width: 1100px;
    height: 640px;
    pointer-events: none;
  }
</style>
</head>
<body>
  <div class="card">
    <svg class="swoosh" viewBox="0 0 1100 640" aria-hidden="true">
      <path fill="var(--swoosh-grey)" d="M0,560 C300,490 620,575 1100,470 L1100,488 C620,600 300,520 0,580 Z"/>
      <path fill="var(--brand-blue)" d="M0,600 C320,540 620,610 1100,505 L1100,640 L0,640 Z"/>
    </svg>

    <div class="brand">
      <span class="brand-dot"></span>
      <span class="brand-name">Quillan Bay Clinics</span>
    </div>

    <div class="person">
      <div class="person-name">Doreen T. Falkner</div>
      <div class="person-title">Chief Operations Officer</div>
      <div class="person-address">837 Township Lane 212<br>Brookvale, GA 30114</div>
    </div>

    <div class="divider"></div>

    <ul class="contacts">
      <li>
        <svg class="icon" viewBox="0 0 24 24"><path d="M6.6 10.8a15.1 15.1 0 0 0 6.6 6.6l2.2-2.2c.3-.3.7-.4 1-.2 1.1.4 2.3.6 3.6.6.6 0 1 .4 1 1V20c0 .6-.4 1-1 1A17 17 0 0 1 3 4c0-.6.4-1 1-1h3.5c.6 0 1 .4 1 1 0 1.3.2 2.5.6 3.6.1.3 0 .7-.2 1z"/></svg>
        404-555-0148
      </li>
      <li>
        <svg class="icon" viewBox="0 0 24 24"><path d="M8 1h8a2 2 0 0 1 2 2v18a2 2 0 0 1-2 2H8a2 2 0 0 1-2-2V3a2 2 0 0 1 2-2zm0 3v14h8V4zm4 15.5a1.2 1.2 0 1 0 0 2.4 1.2 1.2 0 0 0 0-2.4z"/></svg>
        470-555-0193
      </li>
      <li>
        <svg class="icon" viewBox="0 0 24 24"><path d="M7 2h8l3 3v5H7zM4 11h16a2 2 0 0 1 2 2v7a2 2 0 0 1-2 2H4a2 2 0 0 1-2-2v-7a2 2 0 0 1 2-2zm3 4v2h2v-2zm4 0v2h2v-2zm4 0v2h2v-2z"/></svg>
        1-678-555-0126
      </li>
      <li>
        <span class="icon icon-at">@</span>
        quillanbayclinics@mailvista.net
      </li>
      <li>
        <svg class="icon icon-globe" viewBox="0 0 24 24"><circle cx="12" cy="12" r="10"/><ellipse cx="12" cy="12" rx="4.5" ry="10"/><path d="M2 12h20M4 6.5h16M4 17.5h16"/></svg>
        www.quillanbayclinicsco.net
      </li>
    </ul>
  </div>
</body>
</html>
```